General Dental Office Business Card

I run a private general dental office in southern California, and would like a refresh/redesign of my business card. I focus on quality care rather than volume. The email address on the uploaded current card should be updated to: info@marbleshoredental.example. The current card's logo is a deboss, but I am open to other ideas. The logo can be refreshed, but it is something that's been with me since the beginning of the office, so I wouldn't want a drastic redesign.
Target Market(s)
Adults 18-99, whoever needs dental services
Industry/Entity Type
Healthcare/Dental
Contact Information for Business Card
Name, Address, Phone, email
Colors
Designer to choose colors to be used in the design.
Requirements
Must have
- Logo (Same as original one in the uploaded file), space on back for appointment time/date

```html
<!DOCTYPE html>
<html lang="en">
<head>
<meta charset="UTF-8">
<title>Marble Shore Dental — Business Card</title>
<link href="https://fonts.googleapis.com/css2?family=Montserrat:wght@300;400;500&display=swap" rel="stylesheet">
<style>
  :root{
    --bg:#1c1c1f;
    --card:#050505;
    --accent:#86d3ec;
    --ink:#f2f2f2;
    --muted:#8c8c8c;
    --decor:#161616;
    --rule:#d8d8d8;
  }
  *{margin:0;padding:0;box-sizing:border-box}
  html,body{width:1200px;height:800px;overflow:hidden;background:var(--bg)}
  body{font-family:'Montserrat',sans-serif;position:relative}
  .card{
    position:absolute;width:540px;height:309px;background:var(--card);
    overflow:hidden;border-radius:2px;
  }
  .card--front{left:45px;top:200px}
  .card--back{left:615px;top:290px}

  .decor{position:absolute;background:radial-gradient(circle at 50% 50%,#1d1d1d 0%,var(--decor) 60%,transparent 61%)}
  .card--front .decor{right:-90px;top:-120px;width:300px;height:300px}
  .card--back .decor{left:-110px;bottom:-120px;width:320px;height:320px}

  .brand{display:flex;align-items:center;gap:12px}
  .brand__mark{width:62px;height:62px;border-radius:50%;background:var(--accent);flex:none}
  .brand__name{color:var(--accent);font-weight:400;font-size:25px;letter-spacing:.5px;white-space:nowrap}

  .card--front .brand{position:absolute;left:32px;top:38px}
  .contact{position:absolute;left:34px;top:138px;font-size:12.5px;line-height:1.6}
  .contact__address{color:var(--ink);margin-bottom:4px}
  .contact__row{display:flex;align-items:center;gap:9px;color:var(--accent)}
  .contact__row svg{width:12px;height:12px;flex:none}

  .tab{position:absolute;right:0;top:58px;width:22px;height:40px;background:var(--accent)}
  .person{position:absolute;right:42px;top:150px;text-align:right}
  .person__name{color:var(--accent);font-size:18px;font-weight:500}
  .person__title{color:var(--muted);font-size:10px;font-weight:300;margin-top:2px}

  .card--back .brand{position:absolute;left:130px;top:40px}
  .appt{position:absolute;left:110px;top:150px;width:390px;color:var(--ink);font-size:14px}
  .appt__row{display:flex;align-items:flex-end;gap:10px;height:42px}
  .appt__label{width:150px;display:flex;justify-content:space-between}
  .appt__line{flex:1;border-bottom:1px solid var(--rule);margin-bottom:4px}
  .site{position:absolute;right:30px;bottom:26px;color:var(--rule);font-size:12px;font-weight:300;letter-spacing:6px}
</style>
</head>
<body>

<section class="card card--front">
  <div class="decor" role="img" aria-label="Faint large emblem decoration"></div>
  <div class="brand">
    <span class="brand__mark"></span>
    <span class="brand__name">Marble Shore Dental</span>
  </div>
  <div class="contact">
    <p class="contact__address">2180 Harbor Crest Way<br>Seaview, CA 90210</p>
    <p class="contact__row">
      <svg viewBox="0 0 24 24"><path fill="currentColor" d="M6.6 10.8a15 15 0 006.6 6.6l2.2-2.2c.3-.3.7-.4 1-.2 1.1.4 2.3.6 3.6.6.6 0 1 .4 1 1V20c0 .6-.4 1-1 1A17 17 0 013 4c0-.6.4-1 1-1h3.5c.6 0 1 .4 1 1 0 1.3.2 2.5.6 3.6.1.3 0 .7-.2 1z"/></svg>
      555-014-7720
    </p>
    <p class="contact__row">
      <svg viewBox="0 0 24 24"><path fill="currentColor" d="M3 5h18v14H3zm2 2v.5l7 4.5 7-4.5V7zm0 3v7h14v-7l-7 4.5z"/></svg>
      info@marbleshoredental.example
    </p>
    <p class="contact__row">
      <svg viewBox="0 0 24 24"><circle cx="12" cy="12" r="9" fill="none" stroke="currentColor" stroke-width="2"/><path d="M3 12h18M12 3c3 3 3 15 0 18M12 3c-3 3-3 15 0 18" fill="none" stroke="currentColor" stroke-width="1.6"/></svg>
      www.marbleshoredental.example
    </p>
  </div>
  <span class="tab"></span>
  <div class="person">
    <p class="person__name">Daniel R. Moreno DDS</p>
    <p class="person__title">General Dentistry</p>
  </div>
</section>

<section class="card card--back">
  <div class="decor" role="img" aria-label="Faint large emblem decoration"></div>
  <div class="brand">
    <span class="brand__mark"></span>
    <span class="brand__name">Marble Shore Dental</span>
  </div>
  <div class="appt">
    <div class="appt__row"><span class="appt__label"><span>Appointment Date</span><span>:</span></span><span class="appt__line"></span></div>
    <div class="appt__row"><span class="appt__label"><span>Time</span><span>:</span></span><span class="appt__line"></span></div>
  </div>
  <p class="site">www.marbleshoredental.example</p>
</section>

</body>
</html>
```